WP website design (TOVI)

We need a wordpress design that will incorporate a professional color scheme with company logo in a clean layout. The design needs to consider that this will be developed on a responsive theme. Colors are undetermined - those that will complement the logo.
Client mentions liking plinmerbid.com for the layout and use of color. Possible but not necessary to have large slideshow element.

Industry/Entity Type

It Company

Font styles to use
Sans Serif

Colors

Designer to choose colors to be used in the design.

Requirements
Must have
• - Navigation: 1)Home 2) Auctions 3) Services 4) About Us 5) FAQs 6) References 7) Contact Us

Site will have slideshow, please use high-end stock real estate image initially. Header will have logo. Social icons (Facebook, Twitter, Youtube)

Widgets Include: Email signup form, Featured Auctions, Featured Video widget.

Footer will have contact info (below), site navigation, smaller company logo, affiliation logos (attached).

TOVI Auction Group
4275 Birch Vale Lane
Marlowe, KY 40617
1-800-419-BIDS (2437)
Ph. (270) 386-9041
Fx. (270) 386-1158
Nice to have
• - Site will have drop-down menus - please indicate the styling, for instance the dropdown menus 1) Live 2) Online 3) Past - under the 'Auctions' link

```html
<!DOCTYPE html>
<html lang="en">
<head>
<meta charset="utf-8">
<title>TOVI Auction Group</title>
<link href="https://fonts.googleapis.com/css2?family=Roboto+Slab:wght@400;700&family=Arimo:wght@400;700&display=swap" rel="stylesheet">
<style>
:root{
  --red:#d10a0a;
  --nav:#3c3c3c;
  --nav-line:#555;
  --ink:#333;
  --text:#555;
  --line:#d9d9d9;
  --page:#fff;
  --footer:#3d3d3d;
  --footer-bottom:#2b2b2b;
}
*{box-sizing:border-box;margin:0;padding:0}
html,body{width:860px;height:1200px;overflow:hidden;background:var(--page)}
body{position:relative;font-family:"Arimo",Arial,sans-serif;color:var(--text)}
.abs{position:absolute}

/* header */
.hero{left:0;top:0;width:860px;height:342px;
  background:
    linear-gradient(180deg,rgba(255,255,255,0) 60%,rgba(110,100,92,.35) 100%),
    linear-gradient(90deg,#f4f5f5 0%,#e2e0dd 12%,#aaa199 26%,#8e847b 42%,#857b73 58%,#7c7671 72%,#98adc4 86%,#c4d7ea 100%);}
.hero-sky{left:560px;top:0;width:300px;height:200px;
  background:radial-gradient(ellipse at 80% 15%,#a8c8e8 0%,rgba(168,200,232,0) 70%)}
.brand{left:108px;top:84px;display:flex;align-items:center;gap:7px;color:var(--red);font:700 20px/1 "Roboto Slab",Georgia,serif;white-space:nowrap}
.brand-dot{width:12px;height:12px;border-radius:50%;background:var(--red);flex:none}
.phone{left:115px;top:148px;display:flex;align-items:center;gap:6px;font:700 15px "Arimo",sans-serif;color:#333}
.tagline{right:122px;top:212px;text-align:right;color:#fff;font:400 19.5px/24.5px "Roboto Slab",Georgia,serif;text-shadow:0 1px 2px rgba(0,0,0,.35)}

.nav{left:108px;top:309px;width:646px;height:33px;background:var(--nav);display:flex;border-radius:0 3px 3px 0}
.nav a{color:#fff;text-decoration:none;font-size:10.5px;display:flex;align-items:center;justify-content:center;border-left:1px solid var(--nav-line);height:100%}
.nav a:first-child{border-left:0}
.nav .home{width:54px;background:var(--red)}
.band{left:0;top:342px;width:860px;height:28px;background:linear-gradient(180deg,#e4e4e4,#f6f6f6 70%,#fff)}
.band-shadow{left:190px;top:352px;width:480px;height:12px;border-radius:50%;background:radial-gradient(ellipse,rgba(0,0,0,.18),rgba(0,0,0,0) 70%)}

/* welcome */
.welcome-title{left:108px;top:388px;font:400 14.5px "Roboto Slab",serif;color:var(--ink)}
.welcome-title span{color:var(--red)}
.welcome-text{left:108px;top:411px;width:389px;font-size:9.3px;line-height:12.8px;text-align:justify;color:var(--text)}
.read-more{left:453px;top:473px;font-size:9px;font-weight:700;color:var(--red)}
.section-title{left:108px;top:496px;font:400 15px "Roboto Slab",serif;color:var(--ink)}

/* auction cards */
.card{left:108px;width:396px;height:160px;border:1px solid var(--line);border-radius:4px;background:#fff;box-shadow:0 6px 6px -4px rgba(0,0,0,.12)}
.card-title{position:absolute;left:9px;top:9px;font:400 11px "Roboto Slab",serif;color:#444}
.card-photo{position:absolute;left:9px;top:30px;width:112px;height:88px;background:#fff;border:1px solid #ddd;box-shadow:0 2px 3px rgba(0,0,0,.15);padding:4px}
.card-photo div{width:100%;height:100%;background:linear-gradient(180deg,#9aa4ae 0%,#bfc4c8 30%,#b07a5c 50%,#6b5d55 68%,#2f323a 100%)}
.card-sub{position:absolute;left:130px;top:31px;font-size:9.8px;font-weight:700;color:var(--red)}
.card-desc{position:absolute;left:130px;top:50px;width:255px;font-size:9px;line-height:12.5px;color:var(--text)}
.card-meta{position:absolute;left:130px;font-size:9px;color:var(--text)}
.card-meta b{color:var(--red);font-weight:400}
.card-links{position:absolute;left:16px;top:131px;display:flex;gap:10px;font-size:9px;color:#444}
.card-links span{display:flex;align-items:center;gap:3px}
.btn{position:absolute;left:130px;top:124px;width:142px;height:23px;border-radius:3px;background:var(--red);color:#fff;font-size:9.5px;font-weight:700;display:flex;align-items:center;justify-content:center;box-shadow:0 2px 2px rgba(0,0,0,.25)}

/* sidebar */
.widget{left:533px;width:220px;border:1px solid var(--line);border-radius:4px;background:#fff;box-shadow:0 6px 6px -4px rgba(0,0,0,.12)}
.widget-title{position:absolute;left:7px;top:6px;right:7px;padding-bottom:4px;border-bottom:1px solid #eee;font:400 13.5px "Roboto Slab",serif;color:var(--ink)}
.field{position:absolute;width:144px;height:18px;border:1px solid #ddd;font-size:8px;color:#aaa;padding:4px 5px}
.go{position:absolute;width:28px;height:18px;background:var(--red);color:#fff;font-size:10px;font-weight:700;display:flex;align-items:center;justify-content:center;border:1px solid #fff;outline:1px solid #ddd}
.video{position:absolute;left:8px;top:37px;width:202px;height:160px;background:linear-gradient(180deg,#4f5c45 0%,#7d8a72 18%,#d9dbd6 38%,#b9bcb6 50%,#5d5954 68%,#3a3936 100%)}
.play{position:absolute;left:84px;top:70px}
.controls{position:absolute;left:8px;top:197px;width:202px;height:17px;background:#2e2e2e;display:flex;align-items:center;gap:6px;padding:0 5px;font-size:6px;color:#ccc}
.quote{position:absolute;left:10px;font:700 22px Georgia,serif;color:#ccc}
.testimonial{position:absolute;left:27px;width:174px;font-size:8px;line-height:12.8px;color:var(--text)}
.author{position:absolute;left:28px;font-size:9.5px;font-weight:700;color:#444}

/* footer */
.footer{left:0;top:1072px;width:860px;height:102px;background:var(--footer)}
.footer-info{left:110px;top:1084px;font-size:8.6px;line-height:12.3px;color:#fff}
.footer-info p{margin-bottom:4px}
.badge{background:#2a2a2a}
.footer-bottom{left:0;top:1174px;width:860px;height:26px;background:var(--footer-bottom)}
.copyright{left:108px;top:1182px;font-size:8.3px;color:#ddd}
.follow{left:607px;top:1181px;font-size:9.5px;font-weight:700;color:#fff}
.social{top:1178px;width:18px;height:18px;border-radius:3px;background:#6f6f6f}
</style>
</head>
<body>

<div class="abs hero" role="img" aria-label="Stock photo of a large stone two-storey family house with a grey shingle roof under a blue sky with clouds"></div>
<div class="abs hero-sky"></div>

<div class="abs brand"><span class="brand-dot"></span>TOVI Auction Group</div>
<div class="abs phone">
  <svg width="22" height="22" viewBox="0 0 22 22" aria-hidden="true"><circle cx="11" cy="11" r="9.5" fill="#fff" stroke="#d10a0a" stroke-width="2"/><path d="M7.5 6.5c.6-.6 1.3-.5 1.7.1l1 1.6c.3.5.2 1-.2 1.4l-.6.5c.5 1.1 1.3 1.9 2.4 2.5l.5-.6c.4-.4 1-.5 1.4-.2l1.6 1c.6.4.7 1.1.1 1.7-1 1-2.5 1.2-4 .3-2-1.2-3.3-2.6-4.3-4.6-.7-1.4-.5-2.8.4-3.7z" fill="#d10a0a"/></svg>
  270-386-9041
</div>
<div class="abs tagline">Lorem Ipsum Dolor Sit Amet,<br>Consectetuer Adipiscing Elit<br>Sed Diam&nbsp; Lorem</div>

<nav class="abs nav">
  <a class="home" href="#" aria-label="Home"><svg width="16" height="16" viewBox="0 0 16 16"><path d="M8 2 1.5 8h2v6h3.5v-4h2v4H12.5V8h2z" fill="#fff"/></svg></a>
  <a href="#" style="width:115px">AUCTIONS</a>
  <a href="#" style="width:95px">SERVICES</a>
  <a href="#" style="width:96px">ABOUT US</a>
  <a href="#" style="width:83px">FAQs</a>
  <a href="#" style="width:114px">REFERENCES</a>
  <a href="#" style="width:89px">CONTACT US</a>
</nav>
<div class="abs band"></div>
<div class="abs band-shadow"></div>

<h1 class="abs welcome-title">Welcome to <span>TOVI Auction Group</span></h1>
<p class="abs welcome-text">Lorem ipsum dolor sit amet, consectetuer adipiscing elit, sed diam nonummy nibh euisaincidunt ut laoreet dolore magna aliquam erat volutpat. Ut wisi enim ad minim veniam, quis nostruexerci tation ullamcorper suscipit lobortis nisl ut aliquip accumsan et iusto odio enim suscipitdignissim qui blanditent luptatum zzril delenit augue duis dolore te feugait nulla d blanditent luptatum zzril delenit augue duis.</p>
<a class="abs read-more">Read More</a>

<h2 class="abs section-title">Featured Auctions</h2>

<article class="abs card" style="top:520px">
  <h3 class="card-title">ABSOLUTE ONLINE ONLY AUCTION - ANTIQUES &amp; COLLECTIONS</h3>
  <div class="card-photo"><div role="img" aria-label="Photo of a crowd gathered in front of a house at an auction"></div></div>
  <div class="card-sub">Live Off-site Auction with Online bidding</div>
  <p class="card-desc">Lorem ipsum dolor sit amet, consecteuer adiscing elit, sedm nonummy nibh euisaincidunt ut laoreet dolore magna</p>
  <div class="card-meta" style="top:82px"><b>Begins:</b> Tuesday, December 23, 2014 at 1:00 PM EST</div>
  <div class="card-meta" style="top:101px"><b>Location:</b> P.O. Box 51172 Ashgrove, TN 37291</div>
  <div class="card-links">
    <span><svg width="10" height="11" viewBox="0 0 10 11"><rect x="1" y="1" width="7" height="9" fill="none" stroke="#888"/><path d="M3 4h3M3 6h3" stroke="#888"/></svg>Details</span>
    <span><svg width="13" height="11" viewBox="0 0 13 11"><rect x="1" y="2" width="11" height="7" fill="none" stroke="#888"/><path d="M3 2V1M6 2V1M9 2V1" stroke="#888"/></svg>Gallery</span>
  </div>
  <div class="btn">Click here for online bidding</div>
</article>

<article class="abs card" style="top:702px">
  <h3 class="card-title">ABSOLUTE ONLINE ONLY AUCTION - ANTIQUES &amp; COLLECTIONS</h3>
  <div class="card-photo"><div role="img" aria-label="Photo of a crowd gathered in front of a house at an auction"></div></div>
  <div class="card-sub">Live Off-site Auction with Online bidding</div>
  <p class="card-desc">Lorem ipsum dolor sit amet, consecteuer adiscing elit, sedm nonummy nibh euisaincidunt ut laoreet dolore magna</p>
  <div class="card-meta" style="top:82px"><b>Begins:</b> Tuesday, December 23, 2014 at 1:00 PM EST</div>
  <div class="card-meta" style="top:101px"><b>Location:</b> P.O. Box 51172 Ashgrove, TN 37291</div>
  <div class="card-links">
    <span><svg width="10" height="11" viewBox="0 0 10 11"><rect x="1" y="1" width="7" height="9" fill="none" stroke="#888"/><path d="M3 4h3M3 6h3" stroke="#888"/></svg>Details</span>
    <span><svg width="13" height="11" viewBox="0 0 13 11"><rect x="1" y="2" width="11" height="7" fill="none" stroke="#888"/><path d="M3 2V1M6 2V1M9 2V1" stroke="#888"/></svg>Gallery</span>
  </div>
  <div class="btn">Click here for online bidding</div>
</article>

<article class="abs card" style="top:884px">
  <h3 class="card-title">ABSOLUTE ONLINE ONLY AUCTION - ANTIQUES &amp; COLLECTIONS</h3>
  <div class="card-photo"><div role="img" aria-label="Photo of a crowd gathered in front of a house at an auction"></div></div>
  <div class="card-sub">Live Off-site Auction with Online bidding</div>
  <p class="card-desc">Lorem ipsum dolor sit amet, consecteuer adiscing elit, sedm nonummy nibh euisaincidunt ut laoreet dolore magna</p>
  <div class="card-meta" style="top:82px"><b>Begins:</b> Tuesday, December 23, 2014 at 1:00 PM EST</div>
  <div class="card-meta" style="top:101px"><b>Location:</b> P.O. Box 51172 Ashgrove, TN 37291</div>
  <div class="card-links">
    <span><svg width="10" height="11" viewBox="0 0 10 11"><rect x="1" y="1" width="7" height="9" fill="none" stroke="#888"/><path d="M3 4h3M3 6h3" stroke="#888"/></svg>Details</span>
    <span><svg width="13" height="11" viewBox="0 0 13 11"><rect x="1" y="2" width="11" height="7" fill="none" stroke="#888"/><path d="M3 2V1M6 2V1M9 2V1" stroke="#888"/></svg>Gallery</span>
  </div>
  <div class="btn">Click here for online bidding</div>
</article>

<aside class="abs widget" style="top:387px;height:71px">
  <h3 class="widget-title">Auction Search</h3>
  <div class="field" style="left:7px;top:37px">search here......</div>
  <div class="go" style="left:157px;top:37px">GO</div>
</aside>

<aside class="abs widget" style="top:480px;height:228px">
  <h3 class="widget-title">Featured Video</h3>
  <div class="video" role="img" aria-label="Video still of an outdoor auction crowd on a lawn in front of a white house under trees"></div>
  <svg class="play" width="36" height="36" viewBox="0 0 36 36" aria-hidden="true"><circle cx="18" cy="18" r="17" fill="#d10a0a"/><path d="M14 11l12 7-12 7z" fill="#fff"/></svg>
  <div class="controls">
    <svg width="6" height="6"><path d="M0 0l6 3-6 3z" fill="#ddd"/></svg>
    <svg width="7" height="6"><path d="M0 0h1v6H0zM7 0 2 3l5 3z" fill="#ddd"/></svg>
    <svg width="7" height="6"><path d="M0 0l5 3-5 3zM6 0h1v6H6z" fill="#ddd"/></svg>
    <span>00:00</span>
    <span style="flex:1;height:2px;background:#777"></span>
    <span>00:00</span>
    <span style="width:22px;height:2px;background:#d10a0a"></span>
    <svg width="7" height="7"><path d="M0 0h2M0 0v2M7 0H5M7 0v2M0 7h2M0 7V5M7 7H5M7 7V5" stroke="#ddd"/></svg>
  </div>
</aside>

<aside class="abs widget" style="top:729px;height:215px">
  <h3 class="widget-title">Client Testimonials</h3>
  <div class="quote" style="top:28px">&ldquo;</div>
  <p class="testimonial" style="top:32px">Ut wisi enim ad minim veniam, quis nostrud exerc ullamcade orper suscipit lobortis nisl ut aliquip ex ea commodo consequat. Duis autem vel eum. Lorem ipsum is the dummpy text of the insustry.</p>
  <div class="author" style="top:107px">Lorem Ispum, Autem</div>
  <div class="quote" style="top:119px">&ldquo;</div>
  <p class="testimonial" style="top:123px">Ut wisi enim ad minim veniam, quis nostrud exerc ullamcade orper suscipit lobortis nisl ut aliquip ex ea commodo consequat. Duis autem vel eum. Lorem ipsum is the dummpy text of the insustry.</p>
  <div class="author" style="top:196px">Lorem Ispum, Autem</div>
</aside>

<aside class="abs widget" style="top:966px;height:78px">
  <h3 class="widget-title">Newsletter Signup</h3>
  <p style="position:absolute;left:7px;top:30px;width:190px;font-size:8.6px;line-height:10.5px;color:#555">Sign up for our free messages &amp; receive auctions alerts</p>
  <div class="field" style="left:7px;top:55px">email address here......</div>
  <div class="go" style="left:157px;top:55px">GO</div>
</aside>

<footer>
  <div class="abs footer"></div>
  <div class="abs footer-info">
    <p>TOVI Auction Group</p>
    <p>4275 Birch Vale Lane<br>Marlowe, KY 40617</p>
    <p style="margin:0">Toll Free: 1-800-419-BIDS (2437))<br>Phone: 270-386-9041<br>Fax: 270) 386-1158</p>
  </div>
  <div class="abs badge" style="left:446px;top:1100px;width:46px;height:52px;border-radius:2px" role="img" aria-label="Affiliation badge"></div>
  <div class="abs badge" style="left:506px;top:1104px;width:98px;height:44px;border-radius:50%" role="img" aria-label="Affiliation badge"></div>
  <div class="abs badge" style="left:614px;top:1102px;width:58px;height:48px;border-radius:3px" role="img" aria-label="Affiliation badge"></div>
  <div class="abs badge" style="left:690px;top:1094px;width:52px;height:58px;border-radius:2px" role="img" aria-label="Accreditation badge"></div>

  <div class="abs footer-bottom"></div>
  <div class="abs copyright">Copyright &copy; 2014.&nbsp; TOVI Auction Group.&nbsp; All Rights Reserved.</div>
  <div class="abs follow">Follow Us On</div>
  <div class="abs social" style="left:678px" role="img" aria-label="Social link"></div>
  <div class="abs social" style="left:703px" role="img" aria-label="Social link"></div>
  <div class="abs social" style="left:727px" role="img" aria-label="Social link"></div>
</footer>

</body>
</html>
```